Design a Bold Tradeshow Backdrop for a Sustainable Cleaning Technology

We need a professional, high-impact 10' × 8' tradeshow backdrop for Vornelle®, a commercial cleaning technology company. 143.75" x 90" high and needs bleeds in the 143.75" direction for printing but the graphic area is 10' wide.

Our first event will have an audience that includes K–12 school administrators, facility managers, business officials, and custodial decision-makers. However, this backdrop will be used at multiple future trade shows across different commercial and institutional markets.

The design therefore needs to be universal rather than specifically education- or school-themed.

Our goal is to stop attendees as they walk past the booth and immediately communicate a simple message:

Safer and more sustainable cleaning can also cost substantially less than conventional cleaning chemicals.

We want the design to feel modern, innovative, clean, sustainable, credible, commercial, and premium. It should resonate with K–12 decision-makers while being equally appropriate at events serving commercial facilities, healthcare, hospitality, government, property management, transportation, and other institutional markets.

It should NOT look like a traditional janitorial supply advertisement and should not be overly busy.

The most important messages need to be understandable from approximately 10–20 feet away.

Required Messaging

The primary headline should be:

SUSTAINABLE CLEANING
DOES NOT HAVE TO BE EXPENSIVE.

Three major value propositions should be prominently displayed:

FREE
Cleaning Chemical Analysis
See how much you can save.

SAVE UP TO 60% or More
on Cleaning Chemical Costs

AS LITTLE AS $0.27/GALLON

We would also like a strong secondary message incorporated into the design:

SMARTER CLEANING.
High Performance. Low Cost. Safer.

Visual Direction — Important

Rather than showing a K–12 school hallway or other environment that limits the backdrop to the education market, we want a sophisticated, universal commercial or institutional environment.

This could be a bright, contemporary commercial facility, lobby, corridor, office environment, public building, or other premium architectural space that could reasonably represent many different types of facilities.

The environment should communicate:

Cleanliness • Safety • Sustainability • Professionalism • Efficiency • High Performance

We want someone from a school, hospital, hotel, office building, airport, government facility, or other commercial property to be able to look at the backdrop and relate the imagery to their own facility.

Please avoid imagery that makes the backdrop industry-specific.

We also want to avoid clichéd environmental imagery. The design does not need to be covered in leaves, trees, water droplets, recycling symbols, or other obvious "green" graphics to communicate sustainability. We prefer a sophisticated commercial interpretation of sustainability.

Color & Brand Direction

We want the overall color palette to stay primarily within:

Blues — consistent with our corporate identity

Greens — to reinforce sustainability, safety, efficiency, and environmental responsibility

White — strongly encouraged for clean space, contrast, and an open contemporary appearance

Black — should be limited primarily to text where necessary for readability

Please avoid making black a major background or dominant design color.

We want the finished display to have a bright, clean, sophisticated, sustainable look and feel rather than a dark or industrial appearance.

The design should use significant negative space and a strong visual hierarchy.

Less is more.

We prefer a few large, powerful messages that can be understood quickly rather than numerous small bullet points, paragraphs, or icons.

Creative Freedom

The attached concept image is provided to communicate our general direction and messaging only.

It does not need to be copied.

We are specifically running this contest because we want designers to improve upon our initial concept and show us different creative approaches to presenting the Vornelle value proposition.

We are open to creative interpretations of the commercial environment, composition, typography, use of negative space, and how the three major financial benefits are presented.

The finished design should feel like an innovative commercial technology brand, not simply another cleaning chemical company.

Corporate Logo — Very Important

We are attaching our official Vornelle® corporate logo for use in the design.

DO NOT redraw, recreate, modify, stylize, reinterpret, trace, or AI-generate the Vornelle logo.

The supplied corporate logo must be inserted directly into the artwork exactly as provided, maintaining its original proportions, colors, typography, trademark elements, and graphic design.

The logo should generally appear in the upper-left area of the backdrop but should not overwhelm the primary marketing message.

Printer Template & Graphic Sizing

We are also attaching the printer's official graphic template and instructions for the 8' × 8' tension-fabric display.

Designers should create their artwork using these supplied specifications so the winning design can be transferred directly into production.

The printer requires that the original document size not be changed, artwork be created on the designated design layer or a new layer, images be embedded, text be converted to outlines, and the finished production artwork be supplied as a PDF.

Please pay particular attention to the bleed area, finished size, and safe artwork area when positioning important text, graphics, and the corporate logo.

Physical Booth Context

The backdrop will sit behind an 8' tradeshow table.

The complete booth will also contain:

A blue stretch tablecloth with the Vornelle corporate logo
BrevoMax and Vornelle product containers and samples on the table
An HulaDrent chemical mixing/dilution station displayed on an elevated stand to the left
A television/monitor to the right demonstrating our online ROI cost-savings calculator

Because these other booth elements will explain our products and technology in greater detail, the backdrop should NOT attempt to explain everything we do.

Its primary purpose is to stop traffic, establish the Vornelle brand, and communicate our core economic and sustainability value proposition.

Final Deliverables

The winning designer must provide artwork properly sized and positioned using our supplied 8' × 8' tension-fabric display template.

Final files should include:

Print-ready, high-resolution PDF
Editable source/vector artwork
All images embedded
Fonts converted to outlines
Artwork correctly positioned within the supplied printer template
Original Vornelle corporate logo incorporated without modification
The 3–5 Second Test

This is perhaps the most important requirement.

Someone walking down a tradeshow aisle should be able to look at the backdrop for 3–5 seconds and understand:

Vornelle offers safer, sustainable, high-performance commercial cleaning — at a lower cost.

The three offers we particularly want them to remember are:

FREE CHEMICAL ANALYSIS

SAVE UP TO 60%

AS LITTLE AS $0.27/GALLON

The overall takeaway should be:

Sustainable cleaning does not have to cost more.

We want the winning design to make that message immediately understandable, credible, and memorable.

Colors
0054AA
0677BA
7BADD7
CADEEF
E8F1F8
0094D4
00A9DD
6FCCEA
C7EBF8
E9F6FB
00AB8E
00BBA5
67D7C9
C6EFE9
E9F9F6
59FF00
82FF00
B8FF75
E3FFCB
F4FFEA

```html
<!DOCTYPE html>
<html lang="en">
<head>
<meta charset="utf-8">
<title>Vornelle – Sustainable Cleaning Backdrop</title>
<link href="https://fonts.googleapis.com/css2?family=Poppins:ital,wght@0,400;0,500;0,600;0,700;0,800;1,500;1,800&display=swap" rel="stylesheet">
<style>
  :root{
    --brand-blue:#0f56aa;
    --deep-blue:#0054AA;
    --mid-blue:#0677BA;
    --teal:#12b08f;
    --ink:#111418;
    --backdrop:#808184;
  }
  *{margin:0;padding:0;box-sizing:border-box}
  html,body{width:1200px;height:1200px;overflow:hidden;background:var(--backdrop)}
  body{font-family:"Poppins",Arial,sans-serif}
  .panel{position:relative;width:1200px;height:1200px;border-radius:62px 62px 0 0;overflow:hidden;background:#fff}
  .panel-photo{position:absolute;inset:0;
    background:
      linear-gradient(90deg,rgba(255,255,255,1) 0%,rgba(255,255,255,.9) 35%,rgba(255,255,255,0) 65%),
      linear-gradient(90deg,#eef6fa 0%,#cde6ef 70%,#6fc3cc 88%,#a9d6e4 100%)}
  .panel-base{position:absolute;inset:0;width:1200px;height:1200px}
  .brand{position:absolute;left:46px;top:68px}
  .brand-name{font-weight:700;font-size:52px;color:var(--ink);letter-spacing:-1px;line-height:1}
  .headline{position:absolute;left:44px;top:226px;line-height:1}
  .headline-main{display:block;font-weight:800;font-size:86px;color:var(--brand-blue);letter-spacing:-0.5px;line-height:78px}
  .headline-sub{display:block;font-weight:800;font-size:62px;color:var(--teal);letter-spacing:-0.5px;line-height:58px;margin-top:14px}
  .headline-rule{position:absolute;left:46px;top:520px;width:290px;height:5px;background:linear-gradient(90deg,var(--brand-blue) 0%,#6a7ccc 55%,rgba(106,124,204,0) 100%)}
  .offers{position:absolute;left:0;top:571px;width:700px;height:260px}
  .offer{position:absolute;top:0;width:210px;text-align:center}
  .offer-icon{width:82px;height:82px;margin:0 auto;display:block}
  .offer-free{left:15px}
  .offer-save{left:229px}
  .offer-price{left:447px}
  .divider{position:absolute;top:30px;width:2px;height:212px;background:var(--teal)}
  .divider-a{left:228px}.divider-b{left:442px}
  .offer-big{font-weight:800;color:var(--brand-blue);line-height:1}
  .offer-lead{font-weight:700;color:var(--brand-blue);font-size:24px;line-height:1;margin-top:18px}
  .offer-free .offer-big{font-size:68px;margin-top:14px}
  .offer-save .offer-big,.offer-price .offer-big{font-size:66px;margin-top:2px;letter-spacing:-1px}
  .offer-note{font-weight:600;font-size:15px;color:var(--ink);line-height:18px}
  .offer-free .offer-note{margin-top:6px}
  .offer-hint{font-style:italic;font-weight:500;font-size:15px;color:var(--brand-blue);line-height:18px}
  .offer-more{font-weight:600;font-size:24px;color:var(--ink);line-height:1;margin-top:2px}
  .offer-unit{font-weight:600;font-size:24px;color:var(--ink);line-height:1;margin-top:2px}
  .section-rule{position:absolute;left:52px;top:840px;width:600px;height:2px;background:linear-gradient(90deg,rgba(18,176,143,0) 0%,var(--teal) 40%,rgba(18,176,143,0) 100%)}
  .tagline{position:absolute;left:47px;top:866px;width:600px;text-align:center}
  .tagline-head{font-style:italic;font-weight:800;font-size:34px;color:var(--brand-blue);line-height:38px}
  .tagline-sub{font-weight:600;font-size:24px;color:var(--ink);line-height:30px}
</style>
</head>
<body>
<main class="panel">
  <div class="panel-photo" role="img" aria-label="Bright contemporary glass-walled commercial lobby, fading to white on the left"></div>

  <svg class="panel-base" viewBox="0 0 1200 1200" aria-hidden="true">
    <defs>
      <linearGradient id="baseBand" x1="0" y1="0" x2="1" y2="0">
        <stop offset="0" stop-color="#0a52a8"/>
        <stop offset=".65" stop-color="#0e5fb0"/>
        <stop offset="1" stop-color="#12a593"/>
      </linearGradient>
    </defs>
    <path d="M0,1010 Q600,930 1200,960 L1200,1200 L0,1200 Z" fill="url(#baseBand)"/>
  </svg>

  <header class="brand">
    <span class="brand-name">Vornelle®</span>
  </header>

  <h1 class="headline">
    <span class="headline-main">SUSTAINABLE<br>CLEANING</span>
    <span class="headline-sub">DOES NOT HAVE TO<br>BE EXPENSIVE.</span>
  </h1>
  <div class="headline-rule"></div>

  <section class="offers">
    <div class="offer offer-free">
      <svg class="offer-icon" viewBox="0 0 82 82" aria-hidden="true">
        <circle cx="41" cy="41" r="41" fill="var(--teal)"/>
        <path d="M34,20 h14 M36,20 v16 l-12,22 a3,3 0 0 0 3,4 h28 a3,3 0 0 0 3,-4 l-12,-22 v-16" fill="none" stroke="#fff" stroke-width="3.5" stroke-linejoin="round" stroke-linecap="round"/>
        <path d="M29,50 L53,50 L57,58 L25,58 Z" fill="#fff"/>
        <circle cx="36" cy="45" r="2" fill="#fff"/><circle cx="44" cy="42" r="1.6" fill="#fff"/>
      </svg>
      <div class="offer-big">FREE</div>
      <div class="offer-note">Cleaning Chemical<br>Analysis</div>
      <div class="offer-hint">See how much<br>you can save.</div>
    </div>
    <div class="divider divider-a"></div>
    <div class="offer offer-save">
      <svg class="offer-icon" viewBox="0 0 82 82" aria-hidden="true">
        <circle cx="41" cy="41" r="41" fill="var(--teal)"/>
        <rect x="22" y="44" width="6" height="14" fill="#fff"/>
        <rect x="32" y="38" width="6" height="20" fill="#fff"/>
        <rect x="42" y="42" width="6" height="16" fill="#fff"/>
        <rect x="52" y="34" width="6" height="24" fill="#fff"/>
        <path d="M20,38 L32,28 L42,34 L60,20" fill="none" stroke="#fff" stroke-width="3.5" stroke-linejoin="round"/>
        <path d="M52,19 L62,18 L61,28 Z" fill="#fff"/>
      </svg>
      <div class="offer-lead">SAVE UP TO</div>
      <div class="offer-big">60%</div>
      <div class="offer-more">or More</div>
      <div class="offer-note">on Cleaning<br>Chemical Costs</div>
    </div>
    <div class="divider divider-b"></div>
    <div class="offer offer-price">
      <svg class="offer-icon" viewBox="0 0 82 82" aria-hidden="true">
        <circle cx="41" cy="41" r="41" fill="var(--teal)"/>
        <text x="41" y="56" text-anchor="middle" font-family="Poppins, Arial, sans-serif" font-weight="800" font-size="44" fill="#fff">$</text>
      </svg>
      <div class="offer-lead">AS LITTLE AS</div>
      <div class="offer-big">$0.27</div>
      <div class="offer-unit">/GALLON</div>
    </div>
  </section>

  <div class="section-rule"></div>

  <section class="tagline">
    <p class="tagline-head">SMARTER CLEANING.</p>
    <p class="tagline-sub">High Performance. Low Cost. Safer.</p>
  </section>
</main>
</body>
</html>
```